Business supporting small business needs: Business card, A4 letterhead, A6 postcard, C5& C6envelope

We require stationery designed for a new Australian company called "Lanternfield Works" that provides operational strategy and support to small businesses.

We already have a logo (attached).

We require:
- business card (double-sided)
- A4 letterhead (double-sided)
- A6 postcard - to be used like a with-compliments slip (double-sided)
- C5 envelope
- C6 envelope

We would like the backs of the business card, letterhead and postcard to strongly feature the blue colour from the logo.

The business card, letterhead and postcard must contain:
- Lanternfield Works
- Staff member name
- Website address
- Email address
- Phone number
- Postal address
(I will provide these details to the winner)

The letterhead must also contain the ABN: 63 508 217 940 and company name "Lanternfield Works Pty Ltd".

Our standard font is century gothic.

Thank you for the designs so far.

Please note that the only change to the logo I am open to, is using an all white logo on a blue background.

I am not open to any other changes to the logo, such as shading, shadows or other colour changes.

Small and micro business owners

Small Business

```html
<!DOCTYPE html>
<html lang="en">
<head>
<meta charset="utf-8">
<title>Lanternfield Works – Business Card</title>
<link rel="stylesheet" href="https://fonts.googleapis.com/css2?family=Open+Sans:wght@400;600;700&display=swap">
<style>
  :root {
    --brand-blue: #29b0cf;
    --card-white: #ffffff;
    --ink: #1e1e1e;
    --ink-soft: #3a3a3a;
    --backdrop: #e9e6e2;
  }
  * { margin: 0; padding: 0; box-sizing: border-box; }
  html, body {
    width: 1200px; height: 412px; overflow: hidden;
    background: var(--backdrop);
    font-family: "Open Sans", Arial, sans-serif;
  }
  .canvas { position: relative; width: 1200px; height: 412px; }
  .card {
    position: absolute; top: 47px; height: 313px;
    border-radius: 18px; overflow: hidden;
  }
  .card-front { left: 35px; width: 545px; background: var(--card-white); }
  .card-back { left: 600px; width: 547px; background: var(--brand-blue); }

  .wordmark {
    position: absolute; font-weight: 600; white-space: nowrap;
    letter-spacing: 0.5px; display: flex; align-items: center; gap: 12px;
  }
  .wordmark .dot { width: 14px; height: 14px; border-radius: 50%; background: currentColor; }
  .card-front .wordmark { left: 0; right: 0; top: 98px; justify-content: center; font-size: 40px; color: var(--brand-blue); }
  .card-back .wordmark { left: 0; right: 0; top: 118px; justify-content: center; font-size: 42px; color: var(--card-white); }

  .band { position: absolute; left: 0; top: 183px; width: 545px; height: 85px; }

  .person { position: absolute; left: 13px; top: 212px; font-size: 16px; color: var(--ink); white-space: nowrap; }
  .person .name { font-weight: 700; }
  .person .role { font-size: 13px; color: var(--ink-soft); }

  .contact {
    position: absolute; left: 277px; top: 187px; list-style: none;
    font-size: 12.5px; color: var(--ink); line-height: 19.5px; white-space: nowrap;
  }
  .contact li { display: flex; align-items: center; gap: 6px; }
  .contact svg { width: 11px; height: 11px; flex: none; }
  .contact .web { font-weight: 700; }

  .back-url { position: absolute; left: 0; right: 0; top: 263px; text-align: center; font-size: 15px; color: var(--ink-soft); }
</style>
</head>
<body>
<main class="canvas">
  <section class="card card-front" aria-label="Business card front">
    <div class="wordmark"><span class="dot"></span>Lanternfield Works</div>

    <svg class="band" viewBox="0 0 545 85" aria-hidden="true">
      <polygon points="0,0 263,0 178,85 0,85" fill="var(--brand-blue)"/>
      <polygon points="275,0 545,0 545,85 190,85" fill="var(--brand-blue)"/>
    </svg>

    <p class="person"><span class="name">Name Here</span> <span class="role">| Designation</span></p>

    <ul class="contact">
      <li><svg viewBox="0 0 12 12"><path d="M2.5 1 L4.5 1 L5.2 3.4 L4 4.4 Q5 6.8 7.6 8 L8.6 6.8 L11 7.5 L11 9.5 Q10.5 11 9 11 Q1 10 1 2.5 Q1 1 2.5 1Z" fill="var(--ink)"/></svg>015.482.3067</li>
      <li><svg viewBox="0 0 12 12"><rect x="0.8" y="2.5" width="10.4" height="7" fill="none" stroke="var(--ink)" stroke-width="1.2"/><path d="M0.8 2.5 L6 6.5 L11.2 2.5" fill="none" stroke="var(--ink)" stroke-width="1.2"/></svg>name@lanternfieldworks.com</li>
      <li class="web"><svg viewBox="0 0 12 12"><circle cx="6" cy="6" r="5" fill="none" stroke="var(--ink)" stroke-width="1.2"/><ellipse cx="6" cy="6" rx="2.2" ry="5" fill="none" stroke="var(--ink)" stroke-width="1"/><path d="M1 6 H11" stroke="var(--ink)" stroke-width="1"/></svg>www.lanternfieldworks.com</li>
      <li>Lanternfield Works, City, Country-012345</li>
    </ul>
  </section>

  <section class="card card-back" aria-label="Business card back">
    <div class="wordmark"><span class="dot"></span>Lanternfield Works</div>
    <p class="back-url">www.lanternfieldworks.com</p>
  </section>
</main>
</body>
</html>
```